Tour Guide in Israel business card

I am a tour guide in Israel (the holy land). Prior to it I have over 20 years high-tech business. My main (but not only) focus is working with business people that come to Israel and want to get a tour (usually short from few hours to 2 days). During my guiding I incorporate a lot of my know how of the Israeli business culture. I like to have a business card that I can present to anyone that is looking for a tour guide, but that business people will understand the additional value I can provide them during my tour.

Target Market(s)

Business visitors and tourist to Israel

Industry/Entity Type

Tourism

Contact Information for Business Card

Rory Talbeck
email: rory@talbeck-mail.net
Mobile: +972-52-7164059

Colors

Designer to choose colors to be used in the design.

Requirements
Must have
• Tour Guide
Nice to have
• I don't know how but it should project my understanding in business not just the tourist side of my knowledge.

```html
<!DOCTYPE html>
<html lang="en">
<head>
<meta charset="utf-8">
<title>Rory Talbeck – Business Card</title>
<link rel="stylesheet" href="https://fonts.googleapis.com/css2?family=Roboto+Condensed:wght@300;400;700&family=Roboto:wght@400&display=swap">
<style>
  :root {
    --page-bg: #9e9d9e;
    --card-white: #f4f4f4;
    --accent-bar: #c0c0c0;
    --navy: #133f61;
    --text-grey: #4a4a4a;
    --deep-top: #125f8e;
    --deep-bottom: #061a2a;
    --label-blue: #6e89a0;
    --glow: #5cc9f0;
  }
  * { margin: 0; padding: 0; box-sizing: border-box; }
  html, body { width: 1200px; height: 946px; overflow: hidden; }
  body { background: var(--page-bg); position: relative; font-family: "Roboto Condensed", sans-serif; }

  .card {
    position: absolute;
    top: 177px;
    width: 330px;
    height: 594px;
    box-shadow: 1px 2px 3px rgba(0,0,0,0.25);
  }
  .card--front { left: 233px; background: var(--card-white); }
  .card--back {
    left: 638px;
    background: linear-gradient(180deg, var(--deep-top) 0%, #0c3d5e 45%, var(--deep-bottom) 100%);
  }

  .accent-bar {
    position: absolute; left: 0; top: 273px; width: 29px; height: 321px;
    background: var(--accent-bar);
  }
  .name { position: absolute; left: 60px; top: 266px; color: var(--navy); line-height: 1; }
  .name__first { display: block; font-weight: 300; font-size: 46px; letter-spacing: -0.5px; }
  .name__last { display: block; font-weight: 700; font-size: 46px; margin-top: 7px; letter-spacing: -0.5px; }
  .role {
    position: absolute; left: 61px; top: 362px;
    font-weight: 300; font-size: 21px; color: var(--text-grey);
  }
  .contact {
    position: absolute; left: 61px; top: 452px; list-style: none;
    font-weight: 300; font-size: 20px; color: var(--text-grey); line-height: 30.5px;
  }

  .network-map {
    position: absolute; left: 98px; top: 77px; width: 140px; height: 362px;
    border-radius: 40% 45% 35% 40%;
    background: radial-gradient(ellipse at 50% 45%, rgba(92,201,240,0.45) 0%, rgba(40,130,190,0.25) 55%, rgba(18,95,142,0) 75%);
  }
  .theme {
    position: absolute; font-family: "Roboto Condensed", sans-serif; font-weight: 300;
    font-size: 18px; color: var(--label-blue); white-space: nowrap;
    transform-origin: center;
  }
  .theme--land { left: 148px; top: 68px; transform: rotate(-14deg); }
  .theme--history { left: 200px; top: 176px; transform: rotate(80deg); }
  .theme--people { left: 76px; top: 192px; transform: rotate(-68deg); }
  .theme--business { left: 188px; top: 286px; transform: rotate(86deg); }
  .theme--culture { left: 50px; top: 322px; transform: rotate(-80deg); }
  .theme--faith { left: 90px; top: 400px; transform: rotate(-80deg); }

  .tagline {
    position: absolute; left: 0; right: 0; top: 516px; text-align: center;
    font-family: "Roboto", sans-serif; font-size: 19px; letter-spacing: 1px;
    color: var(--glow);
  }
</style>
</head>
<body>
  <section class="card card--front">
    <div class="accent-bar"></div>
    <h1 class="name">
      <span class="name__first">RORY</span>
      <span class="name__last">TALBECK</span>
    </h1>
    <p class="role">Tour Guide &amp; Storyteller</p>
    <ul class="contact">
      <li>+972-52-7164059</li>
      <li>rory@talbeck-mail.net</li>
      <li>www.talbeck-tours.net</li>
    </ul>
  </section>

  <section class="card card--back">
    <div class="network-map" role="img" aria-label="Map of Israel drawn as a glowing network of connected dots"></div>
    <span class="theme theme--land">Land</span>
    <span class="theme theme--history">History</span>
    <span class="theme theme--people">People</span>
    <span class="theme theme--business">Business</span>
    <span class="theme theme--culture">Culture</span>
    <span class="theme theme--faith">Faith</span>
    <p class="tagline">CONNECTING THE DOTS</p>
  </section>
</body>
</html>
```